Business card needed for home based pen making business.

I'm after a business card that's a bit more than an off the shelf card. I do like the idea of a card split horizontal with different colours used. A third colour is to be used for the business name and if need a forth for the other details.

I don't have a logo and will pay extra for one ($150 extra). I mainly make pens and seam rippers (stitch unpicks). The logo may be used for a website in future, as will the colours so please provide the colour codes and font type.

I'd like the business name in an easy to read script font at the top (with logo if you have one) and the other details to the bottom left hand side. I'll leave it up to you to match the script to the font used for the other details.

I'd like to keep a triangular balance to the card so something like a siloet of pot containing pens on the bottom right could be used to balance it out. There my ideas I want to see your.

Business name: Quillo & Co
Email address: quilloandco@mailvista.net
Contact: Dorian
Phone: 0418 352 976
No address is to be used on card.

Target Market(s)

Wide variety of people visiting craft markets. Age range 30+.

Industry/Entity Type

Business

Contact Information for Business Card

Quill & Co

Font styles to use
Script

Colors
f0ecf4
3277b5
3176b5

Requirements
Must have
• Contact: Dorian
• Phone: 0418 352 976
• Email address: quilloandco@mailvista.net
Nice to have
• An icon and/or graphics depicting pens and seam rippers..
Should not have
• I don't want icon/ graphic to be a crossed pen and seam ripper.

```html
<!DOCTYPE html>
<html lang="en">
<head>
<meta charset="utf-8">
<title>Quillo &amp; Co — Business Card</title>
<link rel="stylesheet" href="https://fonts.googleapis.com/css2?family=Questrial&display=swap">
<style>
  :root {
    --brand-blue: #3277b5;
    --brand-blue-deep: #2a67a0;
    --lavender-white: #f0ecf4;
    --paper: #ffffff;
    --ink: #111111;
    --band-dark: #0c0c0c;
    --band-grey: #2b2b2b;
    --rule: rgba(255,255,255,0.55);
    --stage: #e4e1e8;
  }
  * { box-sizing: border-box; margin: 0; padding: 0; }
  html, body {
    width: 1200px; height: 900px; overflow: hidden;
    background: var(--stage);
    font-family: "Questrial", "Century Gothic", sans-serif;
  }
  .canvas { position: relative; width: 1200px; height: 900px; }

  .card {
    position: absolute; left: 280px;
    width: 640px; height: 366px;
    border-radius: 24px; overflow: hidden;
    box-shadow: 0 10px 28px rgba(0,0,0,0.18);
  }

  /* Front */
  .card--front { top: 56px; background: linear-gradient(160deg, #3a80be 0%, var(--brand-blue) 55%, var(--brand-blue-deep) 100%); color: var(--paper); }
  .front__name {
    position: absolute; left: 0; right: 0; top: 138px;
    text-align: center; font-size: 64px; letter-spacing: 1px;
    color: var(--paper);
  }
  .front__social {
    position: absolute; right: 44px; top: 74px;
    display: flex; align-items: center; gap: 8px;
    font-size: 15px; color: var(--paper);
  }
  .front__social .dot { width: 14px; height: 14px; background: var(--paper); border-radius: 2px; }

  /* Back */
  .card--back { top: 478px; background: var(--paper); }
  .back__corner {
    position: absolute; right: 0; top: 0; width: 120px; height: 190px;
    background: var(--brand-blue);
    clip-path: polygon(100% 0, 100% 100%, 86% 100%, 40% 0);
  }
  .back__name-mark {
    position: absolute; left: 0; right: 0; top: 64px;
    text-align: center; font-size: 56px; color: var(--ink);
  }
  .back__band {
    position: absolute; left: 0; right: 0; top: 190px; height: 44px;
    background: var(--band-dark);
  }
  .back__band .band__icon-col {
    position: absolute; left: 0; top: 0; width: 62px; height: 100%;
    background: var(--band-grey);
  }
  .back__band .band__name {
    position: absolute; left: 200px; top: 8px;
    font-size: 26px; letter-spacing: 4px; color: var(--paper);
  }
  .back__contacts {
    position: absolute; left: 0; right: 0; top: 234px; bottom: 0;
    background: linear-gradient(170deg, #3a80be, var(--brand-blue));
  }
  .contact {
    position: relative; height: 44px;
    display: flex; align-items: center;
    border-bottom: 1px solid var(--rule);
    color: var(--paper); font-size: 19px; letter-spacing: 1.5px;
  }
  .contact:last-child { border-bottom: none; }
  .contact__icon {
    width: 62px; height: 100%;
    display: flex; align-items: center; justify-content: center;
    background: rgba(255,255,255,0.14);
    margin-right: 22px;
  }
  .contact__icon svg { width: 22px; height: 22px; }
</style>
</head>
<body>
<main class="canvas">

  <section class="card card--front" aria-label="Card front">
    <div class="front__social"><span class="dot"></span>Quillo &amp; Co</div>
    <h1 class="front__name">Quillo &amp; Co</h1>
  </section>

  <section class="card card--back" aria-label="Card back">
    <div class="back__corner"></div>
    <h2 class="back__name-mark">Quillo &amp; Co</h2>

    <div class="back__band">
      <div class="band__icon-col"></div>
      <span class="band__name">Dorian</span>
    </div>

    <div class="back__contacts">
      <div class="contact contact--phone">
        <span class="contact__icon">
          <svg viewBox="0 0 24 24" fill="#fff"><path d="M4 7c0-2 2-3 8-3s8 1 8 3v2h-4V7H8v2H4z"/><rect x="5" y="11" width="14" height="9" rx="2"/><circle cx="12" cy="15.5" r="2.4" fill="#3277b5"/></svg>
        </span>
        0418 352 976
      </div>
      <div class="contact contact--email">
        <span class="contact__icon">
          <svg viewBox="0 0 24 24" fill="none" stroke="#fff" stroke-width="1.8"><rect x="3" y="6" width="18" height="12"/><path d="M3 6l9 7 9-7"/></svg>
        </span>
        quilloandco@mailvista.net
      </div>
      <div class="contact contact--web">
        <span class="contact__icon">
          <svg viewBox="0 0 24 24" fill="none" stroke="#fff" stroke-width="1.6"><circle cx="12" cy="12" r="9"/><ellipse cx="12" cy="12" rx="4" ry="9"/><path d="M3 12h18M5 7h14M5 17h14"/></svg>
        </span>
        www.quilloandco.com.au
      </div>
    </div>
  </section>

</main>
</body>
</html>
```